Buch-/eBook-Cover Genre: Literarischer Essay, Kulturgeschichte, Autobiografie
Zielgruppe
Wir sind ein Buchverlag und suchen ein ansprechendes Buchcover, welches gut zum Inhalt des Buches passt, den potenziellen Leser anspricht und eine vermarktbare Optik besitzt.
Aufgabenstellung
Projekt-Übersicht
Titel: Oma und die tausend Lieder
Untertitel: Kulturgeschichte des Großvaters
Autor: Gerhard Lindner
Format: 12,5 x 19,0 cm (Taschenbuch)
Genre: Literarischer Essay, Kulturgeschichte, Autobiografie
Über das Buch
Ein über 80-jähriger Autor unternimmt eine kulturhistorische und persönliche Reise durch die Großvaterrolle – von Renaissance-Gemälden bis zur Gegenwart. In der Tradition Montaignes verbindet er Reflexionen über seine drei Enkelkinder mit Analysen historischer Darstellungen. Das Werk bewegt sich zwischen Liebeserklärung, Selbstbefragung und intellektuellem Diskurs über Weitergabe, Loslassen und die Spannung zwischen Idealisierung und Realität.
Tonalität: Nachdenklich aber warmherzig, intellektuell aber zugänglich, würdevoll mit historischer Tiefe
Zielgruppe: Bildungsbürgerliches Publikum (50+), literarisch interessierte Leser, gehobenes Sachbuch-Segment
Design-Konzept
Hauptmotiv: Portrait-Text-Collage
Grundaufbau (siehe Referenzbild):
Kohlezeichnung eines Großvater-Profils (Seitenansicht, nach rechts blickend)
Portrait klar erkennbar mit charakteristischen Details (Falten, Haar, würdevoller Ausdruck)
Handschriftlicher Text als überlagerte Ebene (Palimpsest-Effekt)
Text ergänzt das Portrait, formt es aber nicht (kein Typografie-Portrait!)
Stil & Ästhetik
Portrait:
Kohle-/Bleistiftzeichnung-Ästhetik
Handwerklich, authentisch (nicht digital-glatt)
Verschiedene Tonwerte: von zarten Linien bis zu dunklen Schattierungen
Würdevoll-realistisch, nicht idealisiert
Nach rechts blickend = Zukunft, die Enkelgeneration
Text-Ebene:
Handschriftliche Schreibschrift (persönlicher Charakter)
In verschiedenen Größen, Richtungen und Transparenzen
Teils gut lesbar, teils als Textur
Liegt über/hinter dem Portrait, fließt um Gesichtszüge
Wie Notizen, Tagebucheinträge, Gedankenströme
Einzelne Schlüssel..
Das Design darf nicht zu überladen sein.

```html
<!DOCTYPE html>
<html lang="de">
<head>
<meta charset="utf-8">
<title>Oma und die tausend Lieder – Buchcover</title>
<link href="https://fonts.googleapis.com/css2?family=Roboto:wght@500;700&family=Almendra:wght@700&family=Great+Vibes&family=Reenie+Beanie&family=Cormorant+Garamond:ital,wght@1,600&display=swap" rel="stylesheet">
<style>
  :root {
    --paper-light: #f6e7c6;
    --paper-mid: #e9cf9c;
    --paper-edge: #b98f58;
    --ink-brown: #6f4d2e;
    --ink-dark: #4a3320;
    --ink-soft: #a07e58;
    --ink-faint: rgba(120, 90, 60, 0.35);
    --sketch-dark: #5b4a38;
    --sketch-light: #d9c7a6;
  }
  * { margin: 0; padding: 0; box-sizing: border-box; }
  html, body { width: 789px; height: 1200px; overflow: hidden; background: var(--paper-mid); }
  .cover {
    position: relative;
    width: 789px; height: 1200px;
    overflow: hidden;
    background:
      radial-gradient(ellipse 70% 60% at 60% 35%, var(--paper-light) 0%, transparent 70%),
      radial-gradient(ellipse 120% 100% at 50% 50%, var(--paper-mid) 45%, var(--paper-edge) 100%);
  }
  .portrait {
    position: absolute;
    left: 0; top: 190px;
    width: 460px; height: 1010px;
    background:
      radial-gradient(ellipse 60% 40% at 30% 30%, rgba(91, 74, 56, 0.45) 0%, transparent 70%),
      radial-gradient(ellipse 70% 55% at 35% 75%, rgba(91, 74, 56, 0.35) 0%, transparent 75%),
      radial-gradient(ellipse 90% 80% at 20% 50%, var(--sketch-light) 0%, transparent 80%);
    opacity: 0.85;
  }
  .author {
    position: absolute; top: 36px; left: 0; width: 789px;
    text-align: center;
    font: 700 30px "Roboto", sans-serif;
    color: var(--ink-brown);
    padding-right: 40px;
  }
  .title { position: absolute; font-family: "Almendra", serif; font-weight: 700; color: var(--ink-brown); line-height: 1; }
  .title-main { left: 170px; top: 92px; font-size: 140px; }
  .title-join { left: 492px; top: 158px; font-size: 44px; }
  .title-number { left: 66px; top: 212px; font-size: 120px; letter-spacing: -2px; }
  .title-words { left: 232px; top: 318px; font-size: 118px; }
  .subtitle {
    position: absolute; top: 462px; left: 428px;
    font: 500 23px "Roboto", sans-serif;
    color: var(--ink-dark);
  }
  .note {
    position: absolute;
    font-family: "Reenie Beanie", cursive;
    color: var(--ink-faint);
    text-align: center;
    line-height: 1.05;
  }
  .note-top { left: 175px; top: 535px; width: 420px; font-size: 20px; }
  .note-bottom { left: 390px; top: 1030px; width: 340px; font-size: 18px; color: rgba(90, 60, 30, 0.6); }
  .keyword { position: absolute; font-family: "Great Vibes", cursive; line-height: 1; }
  .keyword-grandfather { left: 320px; top: 665px; font-size: 72px; color: rgba(150, 120, 85, 0.55); letter-spacing: 3px; }
  .keyword-grandchild { left: 488px; top: 835px; font-size: 86px; color: var(--ink-brown); }
  .keyword-wisdom { left: 0; top: 855px; font-size: 52px; color: rgba(120, 95, 70, 0.35); letter-spacing: 4px; }
  .keyword-love { left: 0; top: 1085px; font-size: 68px; color: rgba(120, 95, 70, 0.35); letter-spacing: 4px; }
  .quote {
    position: absolute; left: 340px; top: 752px; width: 480px;
    font: italic 600 20px/1.3 "Cormorant Garamond", serif;
    color: var(--ink-soft);
    text-align: center;
    transform: translateX(-50px);
  }
</style>
</head>
<body>
  <main class="cover">
    <div class="portrait" role="img" aria-label="Kohlezeichnung eines nachdenklichen alten Mannes im Profil, die Hand am Kinn"></div>

    <p class="author">Gerhard Lindner</p>

    <h1>
      <span class="title title-main">Oma</span>
      <span class="title title-join">und die</span>
      <span class="title title-number">tausend</span>
      <span class="title title-words">Lieder</span>
    </h1>
    <p class="subtitle">Kulturgeschichte des Großvaters</p>

    <p class="note note-top">Ich will kein rein wissenschaftliches Buch schreiben, sondern zugleich meine persönliche Reise machen. Bilder und Erinnerungen wurden von meinen alten Gefühlen geprägt. Manchmal beschreibe ich flüchtige Situationen, kaum der Rede wert – für mich allerdings schon</p>

    <span class="keyword keyword-grandfather">Großvate</span>
    <p class="quote">Großvater sein bedeutet, Macht loszulassen, auf formale Autorität zu verzichten, sich zu konzentrieren auf eine Liebe, die der alte Mann an seinen Enkel verschenkt.</p>
    <span class="keyword keyword-grandchild">Enkel</span>
    <span class="keyword keyword-wisdom">Weisheit</span>
    <span class="keyword keyword-love">Liebe</span>

    <p class="note note-bottom">Die Zuwendung zum Enkelkind kann nicht nur eine emotionale Bereicherung sein, sondern auch dessen Stärkung für die Zukunft. Es ist eine Paradoxie des Lebens, dass diese Stärkung des Enkels mit der Hinfälligkeit des Alters verbunden ist</p>
  </main>
</body>
</html>
```